Sign Front of Business

Sign for front of workshop. We want KRT Mechanical in same font and colour as logo then the logo after name. Would like a background colour maybe dark blue with a border.

Target Market(s)

Mining Community

Industry/Entity Type

Mechanical

Requirements
Must have
• Logo colours

```html
<!DOCTYPE html>
<html lang="en">
<head>
<meta charset="utf-8">
<title>KRT Mechanical – Workshop Sign</title>
<link rel="stylesheet" href="https://fonts.googleapis.com/css2?family=Michroma&display=swap">
<style>
  :root {
    --page-bg: #f2f3f5;
    --sign-deep: #0a1f7a;
    --sign-mid: #1636b8;
    --sign-light: #2450d8;
    --frame-light: #e4e6ea;
    --frame-dark: #8c9097;
    --name-silver: #eef1f6;
    --mark-blue: #2f7df0;
  }
  * { box-sizing: border-box; margin: 0; padding: 0; }
  html, body {
    width: 1200px;
    height: 735px;
    overflow: hidden;
    background: var(--page-bg);
  }
  .canvas {
    position: relative;
    width: 1200px;
    height: 735px;
    display: flex;
    align-items: center;
    justify-content: center;
  }
  .sign {
    position: relative;
    width: 1120px;
    height: 168px;
    padding: 6px;
    background: linear-gradient(180deg, var(--frame-light) 0%, var(--frame-dark) 50%, var(--frame-light) 100%);
    box-shadow: 0 4px 14px rgba(0, 0, 0, 0.18);
  }
  .sign__panel {
    position: relative;
    width: 100%;
    height: 100%;
    overflow: hidden;
    display: flex;
    align-items: center;
    padding: 0 46px 0 52px;
    background:
      linear-gradient(135deg, transparent 38%, rgba(60, 110, 255, 0.28) 50%, transparent 62%),
      linear-gradient(45deg, transparent 44%, rgba(60, 110, 255, 0.22) 54%, transparent 64%),
      radial-gradient(ellipse at 55% 50%, var(--sign-light) 0%, var(--sign-mid) 45%, var(--sign-deep) 100%);
  }
  .sign__name {
    font-family: "Michroma", sans-serif;
    font-size: 49px;
    line-height: 1;
    letter-spacing: -1px;
    color: var(--name-silver);
    white-space: nowrap;
  }
  .sign__brand {
    margin-left: auto;
    display: flex;
    align-items: center;
    gap: 12px;
  }
  .sign__brand-dot {
    width: 34px;
    height: 34px;
    border-radius: 50%;
    background: var(--mark-blue);
    flex-shrink: 0;
  }
  .sign__brand-name {
    font-family: "Michroma", sans-serif;
    font-size: 19px;
    line-height: 1.25;
    color: var(--name-silver);
    white-space: nowrap;
  }
</style>
</head>
<body>
  <main class="canvas">
    <section class="sign" aria-label="Workshop front sign">
      <div class="sign__panel">
        <h1 class="sign__name">KRT MECHANICAL</h1>
        <div class="sign__brand">
          <span class="sign__brand-dot"></span>
          <span class="sign__brand-name">KRT Mechanical</span>
        </div>
      </div>
    </section>
  </main>
</body>
</html>
```